Geschäftspapiere für Immobilienmakler
Tolles Design. Schnelle Umsetzung der Änderungswünsche.
Zielgruppe
Wir sind Immobilienmakler und bieten zusätzlich Home Staging an.
https://nordhaus-kellwang.de/Home-Staging/
Um anderen Immobilienmakler oder Privatanbieter unsere Dienstleistung anzubieten, möchten wir ein Anschreiben gestalten lassen. Welches wir hauptsächlich per E-Mail versenden können, da die Postanschrift oft nicht bekannt ist.
Trotzdem bitte auch eine Rückseite gestalten für den Versand per Post.
Aufgabenstellung
Im Anhang ist ein Muster mit Mustertext.
Bitte auch eine Rückseite gestalten für den Versand per Post.
Das Anschreiben/der Infobrief sollte ansprechend schick aussehen.
Ich könne mir vorstellen, dass oben auf der Seite die gleichen Bilder sind wir auf der Homepage.
Oder dies in den Hintergrund miteingearbeitet wird.
(die Lampe, das Bett, die Badezimmerdeko)
Wichtig ist auch dass das Logo mit der Glühbirne, dem Vogel und dem Slogan 'Ins richtige Licht rücken - Werte steigern'
Weiterhin wichtig dass die Vorher-Nachher Bilder gut zur Geltung kommen.
Ich habe als Datei unsere Flyer und eine Mappe zur Ansicht mit angehängt.
Hier sollte es dazu passen.

```html
<!DOCTYPE html>
<html lang="de">
<head>
<meta charset="utf-8">
<title>Nordhaus Kellwang – Anschreiben Home Staging</title>
<link href="https://fonts.googleapis.com/css2?family=Arimo:wght@400;700&family=Montserrat:wght@600;700;800&family=Tinos:wght@400;700&display=swap" rel="stylesheet">
<style>
  :root {
    --navy: #004375;
    --gold: #b8943c;
    --paper: #ffffff;
    --stage: #c8c8c8;
    --ink: #1a1a1a;
    --soft: #f1f1f1;
  }
  * { box-sizing: border-box; margin: 0; padding: 0; }
  html, body { width: 1111px; height: 1200px; overflow: hidden; background: var(--stage); }
  .sheet {
    position: absolute; top: 225px; width: 530px; height: 750px;
    background: var(--paper); overflow: hidden;
  }
  .sheet--front { left: 17px; }
  .sheet--back { left: 564px; }

  /* Front: slogan header */
  .slogan { position: absolute; top: 38px; left: 0; width: 530px; height: 70px; }
  .slogan__rule { position: absolute; top: 35px; height: 2px; background: var(--gold); }
  .slogan__rule--left { left: 73px; width: 98px; }
  .slogan__rule--right { left: 383px; width: 147px; }
  .slogan__text { position: absolute; font-family: 'Montserrat', sans-serif; font-weight: 700; line-height: 18px; }
  .slogan__text--left { right: 270px; top: 27px; text-align: right; font-size: 12.5px; color: var(--navy); }
  .slogan__text--right { left: 312px; top: 27px; font-size: 12.5px; color: var(--navy); }
  .slogan__big { font-size: 15px; color: var(--gold); }
  .slogan__mark { position: absolute; left: 267px; top: 14px; width: 40px; height: 40px; border: 3px solid var(--gold); border-radius: 50%; }

  .return-line { position: absolute; left: 73px; top: 155px; font-family: 'Arimo', sans-serif; font-size: 4.5px; font-weight: 700; color: var(--navy); border-bottom: 0.6px solid var(--navy); letter-spacing: 0.1px; }
  .recipient { position: absolute; left: 73px; top: 166px; font-family: 'Arimo', sans-serif; font-size: 7.4px; line-height: 10.7px; color: var(--ink); }

  .letter { position: absolute; left: 73px; width: 360px; font-family: 'Tinos', serif; font-size: 8.1px; line-height: 12.6px; color: var(--ink); }
  .letter strong { font-weight: 700; }
  .letter p + p { margin-top: 7px; }
  .letter--body { top: 268px; }
  .letter--close { top: 562px; }

  .showcase { position: absolute; left: 0; top: 421px; width: 530px; height: 122px; background: var(--navy); }
  .showcase__hint { position: absolute; left: 27px; top: 10px; font-family: 'Tinos', serif; font-size: 7.8px; color: #fff; }
  .showcase__title { position: absolute; left: 26px; top: 84px; font-family: 'Arimo', sans-serif; font-size: 13.5px; font-weight: 700; color: #fff; }
  .showcase__tag { position: absolute; left: 0; top: 110px; width: 162px; height: 22px; background: var(--gold); padding: 3px 0 0 26px; font-family: 'Arimo', sans-serif; font-size: 13.5px; font-weight: 700; color: #fff; }
  .showcase__photo { position: absolute; top: 8px; width: 151px; height: 106px; }
  .showcase__photo--before { left: 135px; background: linear-gradient(160deg, #eef0ea 0%, #d8d2c4 55%, #b58d5e 100%); }
  .showcase__photo--after { left: 322px; background: linear-gradient(160deg, #eef0ea 0%, #c9c7c0 55%, #6f6a72 100%); }
  .showcase__arrow { position: absolute; left: 270px; top: 45px; }

  .more-info { position: absolute; left: 25px; top: 658px; width: 270px; height: 28px; background: var(--soft); border-radius: 14px; padding: 7px 0 0 48px; font-family: 'Tinos', serif; font-size: 8px; color: var(--ink); }
  .footer-rule { position: absolute; top: 689px; height: 2px; background: var(--gold); }
  .footer-rule--left { left: 0; width: 420px; }
  .footer-rule--right { left: 492px; width: 38px; }
  .contact { position: absolute; top: 700px; font-family: 'Arimo', sans-serif; font-size: 8px; font-weight: 700; line-height: 10.6px; color: var(--navy); }
  .contact--company { left: 72px; }
  .contact--lines { left: 190px; }
  .brand { position: absolute; font-family: 'Montserrat', sans-serif; font-weight: 800; color: var(--navy); white-space: nowrap; }
  .brand--footer { left: 380px; top: 720px; font-size: 11.5px; }

  /* Back */
  .panel { position: absolute; left: 332px; top: 0; width: 198px; height: 750px; background: var(--navy); }
  .tab { position: absolute; left: 0; height: 22px; padding: 3px 14px 0 14px; font-family: 'Arimo', sans-serif; font-weight: 700; font-size: 13px; color: #fff; }
  .tab--navy { top: 48px; background: var(--navy); }
  .tab--gold { top: 76px; background: var(--gold); }
  .back-rule { position: absolute; left: 110px; top: 98px; width: 270px; height: 2px; background: var(--gold); }
  .brand--back { left: 358px; top: 86px; font-size: 14px; color: #fff; }
  .brand-dot { position: absolute; left: 470px; top: 55px; width: 28px; height: 28px; background: var(--gold); border-radius: 50%; }
  .panel-photo { position: absolute; left: 352px; width: 160px; height: 150px; }
  .panel-photo--bed { top: 160px; background: linear-gradient(170deg, #f3f3f1 0%, #d9d7d4 60%, #8c8b8c 100%); }
  .panel-photo--lamp { top: 325px; background: radial-gradient(circle at 45% 35%, #f6d66b 0%, #c99a2f 35%, #8e9092 70%, #d9d9d9 100%); }
  .panel-photo--bath { top: 490px; background: linear-gradient(170deg, #f5f5f5 0%, #e3e0e6 60%, #a98fb0 100%); }
  .refs { position: absolute; left: 348px; top: 655px; font-family: 'Arimo', sans-serif; font-style: italic; font-weight: 700; font-size: 8.5px; color: #fff; }
  .refs-url { position: absolute; left: 345px; top: 672px; width: 170px; height: 22px; background: var(--gold); padding: 4px 0 0 8px; font-family: 'Arimo', sans-serif; font-weight: 700; font-size: 10px; color: #fff; }
  .portrait-rule { position: absolute; left: 0; top: 660px; width: 332px; height: 2px; background: var(--gold); }
  .portrait { position: absolute; top: 580px; width: 128px; height: 90px; }
  .portrait--jana { left: 40px; background: linear-gradient(180deg, #8c9592 0%, #6b6f6b 60%, #8a7a68 100%); }
  .portrait--paul { left: 185px; background: linear-gradient(180deg, #a7a7a5 0%, #5f5f62 60%, #3f4856 100%); }
  .portrait-name { position: absolute; top: 676px; font-family: 'Arimo', sans-serif; font-style: italic; font-weight: 700; font-size: 9px; color: var(--navy); }
  .portrait-name--jana { left: 40px; }
  .portrait-name--paul { left: 185px; }
</style>
</head>
<body>

<section class="sheet sheet--front" aria-label="Anschreiben Vorderseite">
  <header class="slogan">
    <div class="slogan__rule slogan__rule--left"></div>
    <div class="slogan__rule slogan__rule--right"></div>
    <p class="slogan__text slogan__text--left">Ins richtige<br><span class="slogan__big">Licht</span> rücken.</p>
    <div class="slogan__mark"></div>
    <p class="slogan__text slogan__text--right"><span class="slogan__big">Werte</span><br>steigern!</p>
  </header>

  <p class="return-line">NORDHAUS KELLWANG GMBH | LINDENWEG 8 | 12345 MUSTERSTADT</p>
  <address class="recipient" style="font-style:normal">Firma<br>Ansprechpartner<br>Straße Nummer<br>123456 Ort</address>

  <div class="letter letter--body">
    <p>Sehr geehrte Damen und Herren, Liebe Kunden, Liebe Kollegen,</p>
    <p style="margin-top:12px">bei Marktrecherchen ist unserem Backoffice aufgefallen dass wir Ihre Immobilie/Immobilien durch unsere verkaufsfördernden Maßnahmen in ein besseres Licht rücken können.<br><strong>Für einen erfolgreichen und schnelleren Verkauf bieten wir HOME STAGING an.</strong></p>
    <p><strong>Was ist HOME STAGING?</strong><br>HOME STAGING wird das professionelle herrichten von Räumen oder ganzen Immobilie zur Verkaufsförderung genannt. Diese Adaption umfasst den gezielten Einsatz von Möbeln, Dekoration, Farbe, Licht, Wand- und Fußbodengestaltung.<br>Immobilien, die mit HOME STAGING für den Verkauf vorbereitet werden, haben eine viel kürzere Verkaufszeit und einen <strong>höheren Verkaufspreis um ca. 10-15%.</strong></p>
  </div>

  <div class="showcase">
    <p class="showcase__hint">Hier nur ein Beispiel:</p>
    <p class="showcase__title">Vor und nach</p>
    <div class="showcase__photo showcase__photo--before" role="img" aria-label="Leerer Wohnraum vor dem Home Staging"></div>
    <svg class="showcase__arrow" width="46" height="22" viewBox="0 0 46 22" aria-hidden="true">
      <path d="M2 18 Q20 2 40 10" fill="none" stroke="#fff" stroke-width="2.5"/>
      <path d="M34 4 L42 10 L33 15" fill="none" stroke="#fff" stroke-width="2.5"/>
    </svg>
    <div class="showcase__photo showcase__photo--after" role="img" aria-label="Derselbe Wohnraum nach dem Home Staging mit Sofa und Teppich"></div>
  </div>
  <p class="showcase__tag" style="top:531px">dem Home Staging</p>

  <div class="letter letter--close">
    <p><strong>Probieren Sie es aus!</strong><br>Anschließend werden Sie jede Immobilie Home Stagen lassen. Gerne machen wir Ihnen ein unschlagbares Kennenlern-Angebot.</p>
    <p style="margin-top:14px"><strong>Mit freundlichen Grüßen<br>Jana und Paul Kellwang</strong></p>
  </div>

  <p class="more-info">Weitere Infos unter: www.nordhaus-kellwang.de</p>
  <div class="footer-rule footer-rule--left"></div>
  <div class="footer-rule footer-rule--right"></div>
  <p class="contact contact--company">Nordhaus Kellwang<br>GmbH<br>Lindenweg 8<br>12345 Musterstadt</p>
  <p class="contact contact--lines">Tel.: 0 12 34 / 56 78 90<br>Fax: 0 12 34 / 56 78 91<br>kontakt@nordhaus-kellwang.de<br>www.nordhaus-kellwang.de</p>
  <p class="brand brand--footer">Nordhaus Kellwang</p>
</section>

<section class="sheet sheet--back" aria-label="Anschreiben Rückseite">
  <div class="panel"></div>
  <p class="tab tab--navy">verschönern</p>
  <p class="tab tab--gold">Immobilie</p>
  <div class="back-rule"></div>
  <div class="brand-dot"></div>
  <p class="brand brand--back">Nordhaus Kellwang</p>

  <div class="panel-photo panel-photo--bed" role="img" aria-label="Gestaltetes Schlafzimmer mit Bett und Spiegel"></div>
  <div class="panel-photo panel-photo--lamp" role="img" aria-label="Pendelleuchte mit goldenem Innenschirm"></div>
  <div class="panel-photo panel-photo--bath" role="img" aria-label="Helles Badezimmer mit Dekoration"></div>

  <p class="refs">weitere Referenzen finden Sie unter:</p>
  <p class="refs-url">www.nordhaus-kellwang.de</p>

  <div class="portrait-rule"></div>
  <div class="portrait portrait--jana" role="img" aria-label="Porträtfoto Jana Kellwang"></div>
  <div class="portrait portrait--paul" role="img" aria-label="Porträtfoto Paul Kellwang"></div>
  <p class="portrait-name portrait-name--jana">Jana Kellwang</p>
  <p class="portrait-name portrait-name--paul">Paul Kellwang</p>
</section>

</body>
</html>
```